Professional Modern Website Design

We are a premium IT services provider to the financial industry based in London. Our company is called Veltra our current holding page is www.veltra-example.co.uk. We require a new website to match our new corporate identity. This project is for the design phase only. Development will be handled in-house. I have attached examples of wire frames we have developed (although open to suggestions for improvement) Our brand document that should demonstrate current brand, inc how we communicate to potential clients and finally mostly completed web-content.
We are looking for designers that can create something that sets us apart from our competitors.
Target Market(s)
IT Decision makers in Finance companies such as; hedge funds, private investment banks etc
Industry/Entity Type
Financial
Number of Pages Required
5+ page
Requirements
Must have
- hexagon elements in the design, unique design.
Nice to have
- Blog and social media feeds
Should not have
- Should not resemble a downloaded template

```html
<!DOCTYPE html>
<html lang="en">
<head>
<meta charset="utf-8">
<title>Veltra – Systems Integration for Finance</title>
<link href="https://fonts.googleapis.com/css2?family=Fira+Sans:wght@400;500;600;700&display=swap" rel="stylesheet">
<style>
  :root {
    --orange: #f7901e;
    --orange-deep: #ef6a25;
    --page-bg: #f4f2f2;
    --hero-bg: #fafaf3;
    --white: #ffffff;
    --ink: #2b2b2b;
    --ink-soft: #555555;
    --heading: #4a4a4a;
    --yellow: #fcc314;
    --yellow-pale: #fde49a;
  }
  * { margin: 0; padding: 0; box-sizing: border-box; }
  html, body { width: 1200px; height: 1000px; overflow: hidden; }
  body { background: var(--page-bg); font-family: "Fira Sans", Arial, sans-serif; color: var(--ink); position: relative; }
  .site { position: absolute; left: 199px; top: 0; width: 802px; height: 1000px; background: var(--white); }

  .topbar { position: absolute; left: 0; top: 0; width: 802px; height: 40px; }
  .contact-line { position: absolute; right: 46px; top: 14px; font-size: 7px; color: var(--ink-soft); display: flex; gap: 8px; align-items: center; }
  .contact-line span { display: flex; align-items: center; gap: 3px; }
  .contact-line svg { width: 8px; height: 8px; }

  .navband { position: absolute; left: 0; top: 40px; width: 802px; height: 31px; background: var(--orange); }
  .nav { position: absolute; right: 48px; top: 9px; display: flex; gap: 20px; list-style: none; }
  .nav li { color: var(--white); font-size: 10px; font-weight: 500; }

  .brand { position: absolute; left: 44px; top: 0; width: 72px; height: 62px; z-index: 3; filter: drop-shadow(1px 2px 2px rgba(0,0,0,.18)); }
  .brand svg { position: absolute; inset: 0; }
  .brand-name { position: absolute; left: 0; width: 72px; top: 24px; text-align: center; font-size: 13px; font-weight: 600; color: var(--orange-deep); }

  .hero { position: absolute; left: 0; top: 71px; width: 802px; height: 326px; background: var(--hero-bg); }
  .hero-title { position: absolute; left: 50px; top: 70px; width: 230px; font-size: 14px; font-weight: 500; line-height: 17px; color: var(--orange); }
  .hero-copy { position: absolute; left: 51px; top: 118px; width: 210px; font-size: 11px; font-weight: 500; line-height: 14.2px; color: var(--ink-soft); }
  .hero-button { position: absolute; left: 53px; top: 227px; width: 76px; height: 21px; background: var(--orange); color: var(--white); font-size: 11px; font-weight: 600; text-align: center; line-height: 21px; }
  .hero-art { position: absolute; left: 291px; top: 24px; width: 511px; height: 240px; background: radial-gradient(ellipse at 45% 55%, #f3e3d6 0%, #e6ebee 55%, var(--hero-bg) 100%); border-radius: 6px; }
  .slider-arrow { position: absolute; top: 152px; width: 22px; height: 22px; border-radius: 50%; background: var(--orange); }
  .slider-arrow svg { width: 22px; height: 22px; }
  .slider-prev { left: 18px; }
  .slider-next { left: 768px; }

  .intro-badge { position: absolute; left: 358px; top: 370px; width: 72px; height: 72px; border-radius: 50%; background: var(--yellow-pale); }
  .intro-badge::after { content: ""; position: absolute; left: 8px; top: 8px; width: 56px; height: 56px; border-radius: 50%; background: var(--yellow); }
  .intro-badge span { position: absolute; inset: 0; z-index: 1; text-align: center; line-height: 72px; font-size: 34px; font-weight: 700; color: var(--white); }
  .intro-title { position: absolute; left: 0; width: 802px; top: 444px; text-align: center; font-size: 21px; font-weight: 500; color: var(--heading); }
  .intro-lead { position: absolute; left: 120px; width: 562px; top: 478px; text-align: center; font-size: 14px; line-height: 17px; color: var(--ink-soft); }

  .audience { position: absolute; top: 548px; width: 170px; text-align: center; }
  .audience-hex { display: block; margin: 0 auto; width: 138px; height: 154px; }
  .audience-role { margin-top: 10px; font-size: 11.5px; font-weight: 500; color: #111; white-space: nowrap; }
  .audience-text { margin: 14px auto 0; width: 160px; font-size: 8.6px; font-weight: 500; line-height: 11px; color: var(--ink); }
  .aud-1 { left: 46px; } .aud-2 { left: 223px; } .aud-3 { left: 406px; } .aud-4 { left: 585px; }

  .footer { position: absolute; left: 0; top: 886px; width: 802px; height: 114px; background: var(--orange); text-align: center; color: var(--white); }
  .footer-brand { margin-top: 16px; display: inline-flex; align-items: center; gap: 4px; font-size: 11px; font-weight: 600; }
  .footer-brand i { width: 8px; height: 8px; background: var(--orange-deep); display: inline-block; }
  .footer-legal { margin-top: 6px; font-size: 11px; font-weight: 600; line-height: 14px; }
  .social { margin-top: 10px; display: flex; justify-content: center; gap: 4px; list-style: none; }
  .social li { width: 17px; height: 17px; border-radius: 50%; background: var(--orange-deep); border: 1px solid #f9b36a; }
</style>
</head>
<body>
<div class="site">
  <header class="topbar">
    <div class="contact-line">
      <span><svg viewBox="0 0 8 8"><rect x="0" y="1.5" width="8" height="5" fill="#f7901e"/></svg>info@veltra-example.co.uk</span>
      <span><svg viewBox="0 0 8 8"><circle cx="4" cy="4" r="3.5" fill="#f7901e"/></svg>+44 20 0000 1234</span>
    </div>
  </header>

  <div class="brand">
    <svg viewBox="0 0 72 62"><polygon points="0,0 72,0 72,44 36,62 0,44" fill="#ffffff"/></svg>
    <div class="brand-name">Veltra</div>
  </div>

  <nav class="navband">
    <ul class="nav">
      <li>About</li><li>Services</li><li>Partners</li><li>Clients</li><li>Contact</li>
    </ul>
  </nav>

  <section class="hero">
    <h1 class="hero-title">You need integration. We’re always there with you.</h1>
    <p class="hero-copy">Veltra is one of the leading systems integrators to the world’s finance sector. We are an extension of your business and our services portfolio has been built so you always have access to a complete partner.</p>
    <div class="hero-button">About Us</div>
    <div class="hero-art" role="img" aria-label="Flat illustration of IT tools: clocks, lifebuoy, gears, screwdriver held by a hand, traffic cone and tape measure"></div>
    <div class="slider-arrow slider-prev"><svg viewBox="0 0 22 22"><polyline points="13,6 8,11 13,16" fill="none" stroke="#fff" stroke-width="2.2"/></svg></div>
    <div class="slider-arrow slider-next"><svg viewBox="0 0 22 22"><polyline points="9,6 14,11 9,16" fill="none" stroke="#fff" stroke-width="2.2"/></svg></div>
  </section>

  <div class="intro-badge"><span>?</span></div>
  <h2 class="intro-title">Who Are You</h2>
  <p class="intro-lead">If you’re part of a financial organisation, we have the power to help everyone work more efficiently, productively and profitably.</p>

  <svg width="0" height="0" style="position:absolute">
    <defs>
      <linearGradient id="hexRing" x1="0" y1="0" x2="1" y2="1">
        <stop offset="0" stop-color="#ef6a25"/><stop offset="1" stop-color="#f7a21e"/>
      </linearGradient>
      <linearGradient id="hexPhoto" x1="0" y1="0" x2="0" y2="1">
        <stop offset="0" stop-color="#c9d3db"/><stop offset="0.6" stop-color="#9a8d84"/><stop offset="1" stop-color="#3a3f48"/>
      </linearGradient>
    </defs>
  </svg>

  <article class="audience aud-1">
    <svg class="audience-hex" viewBox="0 0 138 154" role="img" aria-label="Portrait photo of a senior hedge fund manager">
      <polygon points="69,4 134,41 134,113 69,150 4,113 4,41" fill="url(#hexPhoto)" stroke="url(#hexRing)" stroke-width="10"/>
    </svg>
    <h3 class="audience-role">Senior Hedge Fund Manager/CEO</h3>
    <p class="audience-text">You need to develop and implement strategies for business growth, while ensuring profitability. You’re aware your biggest asset is your staff and a happy workforce is a productive one. Security is a key concern in a changing always-on world and you need to be compliant, but you don’t want to overspend. Veltra can help you find the best solutions to help your business grow at the speed you want it to.</p>
  </article>

  <article class="audience aud-2">
    <svg class="audience-hex" viewBox="0 0 138 154" role="img" aria-label="Portrait photo of a chief financial officer">
      <polygon points="69,4 134,41 134,113 69,150 4,113 4,41" fill="url(#hexPhoto)" stroke="url(#hexRing)" stroke-width="10"/>
    </svg>
    <h3 class="audience-role">CFO</h3>
    <p class="audience-text">Your key responsibility is to obtain the maximum ROI from products and services. You understand investment opportunities, providing they return higher efficiencies and revenues. You are concerned more with long-term spending versus short-term and how you can get the most value out of a proposition. Veltra can advise how to boost ROI by streamlining your business to maximise return.</p>
  </article>

  <article class="audience aud-3">
    <svg class="audience-hex" viewBox="0 0 138 154" role="img" aria-label="Portrait photo of an IT manager">
      <polygon points="69,4 134,41 134,113 69,150 4,113 4,41" fill="url(#hexPhoto)" stroke="url(#hexRing)" stroke-width="10"/>
    </svg>
    <h3 class="audience-role">IT Manager/CTO</h3>
    <p class="audience-text">Integration with partners and services is your key concern. You want to make sure any IT system you implement will work with the whole infrastructure of your company. You don’t want your team to waste valuable time dealing with things that don’t matter. Veltra provides the whole picture to ensure your company is ready for the next generation of IT.</p>
  </article>

  <article class="audience aud-4">
    <svg class="audience-hex" viewBox="0 0 138 154" role="img" aria-label="Portrait photo of an employee">
      <polygon points="69,4 134,41 134,113 69,150 4,113 4,41" fill="url(#hexPhoto)" stroke="url(#hexRing)" stroke-width="10"/>
    </svg>
    <h3 class="audience-role">Employees</h3>
    <p class="audience-text">You’re working hard, but not getting anywhere fast. You want the tools to make your job easier so you can spend more time thinking about what you’re doing rather than how you’re doing it. You shouldn’t have to think about the technology you’re using, because it should just work. Veltra can help you get back on track everyday.</p>
  </article>

  <footer class="footer">
    <div class="footer-brand"><i></i>Veltra</div>
    <p class="footer-legal">@ Veltra Ltd. Company Registration No.1234567<br>Incorporated in England &amp; Whales</p>
    <ul class="social" aria-label="Social links">
      <li></li><li></li><li></li><li></li><li></li><li></li>
    </ul>
  </footer>
</div>
</body>
</html>
```